A4 Block Hour Agreement Brochure

We need a new Block Hour Agreement Brochure created as our current one lacks design and is ugly. The current block hour agreement brochure has been attached "pixelharbor.pdf".

We are looking at a modern brochure and have attached "Brightmoor Private Cloud Plans.pdf" as an example.

It doesnt have to be the exact same design, but it must be the "Brightmoor blue" theme.

Target Market(s)

Information Technology

Colors
0054AA
0677BA
7BADD7
CADEEF
E8F1F8

```html
<!DOCTYPE html>
<html lang="en">
<head>
<meta charset="utf-8">
<title>Block Hour Agreement – Brightmoor Technologies</title>
<link href="https://fonts.googleapis.com/css2?family=Bebas+Neue&family=Montserrat:wght@400;500;600;700&display=swap" rel="stylesheet">
<style>
  :root {
    --sky: #00b2ee;
    --navy: #2b3192;
    --brand-blue: #0054aa;
    --brand-mid: #0677ba;
    --ink: #1a1a1a;
    --stage: #c6d7e6;
    --paper: #ffffff;
    --row-top: #ffffff;
    --row-bottom: #d2d4d8;
    --panel-dark: #05080d;
  }
  * { margin: 0; padding: 0; box-sizing: border-box; }
  html, body { width: 939px; height: 1200px; overflow: hidden; }
  body { background: var(--stage); font-family: "Montserrat", sans-serif; color: var(--ink); }

  .brochure {
    position: absolute; left: 45px; top: 0; width: 849px; height: 1200px;
    background: linear-gradient(180deg, #f4f4f5 0%, #ffffff 45%, #ffffff 100%);
    overflow: hidden;
  }
  .brochure__photo {
    position: absolute; right: 0; top: 0; width: 246px; height: 100%;
    background:
      radial-gradient(circle at 45% 33%, #9fe6ff 0%, #2aa6e6 9%, #0d5d9c 24%, #0a2e52 40%, transparent 58%),
      linear-gradient(180deg, #05080d 0%, #0a1c30 30%, #0b2540 45%, #05080d 75%, #030407 100%);
  }

  .title { position: absolute; left: 61px; top: 58px; font-family: "Bebas Neue", sans-serif; font-size: 122px; line-height: 94px; letter-spacing: 1px; }
  .title__line--light { color: var(--sky); }
  .title__line--dark { color: var(--navy); }

  .section-heading { position: absolute; left: 61px; font-weight: 700; }
  .section-heading--overview { top: 276px; font-size: 22px; color: var(--sky); }
  .section-heading--types { top: 846px; font-size: 25px; color: var(--navy); }

  .overview { position: absolute; left: 61px; width: 497px; font-size: 12.6px; line-height: 19px; text-align: justify; }
  .overview--intro { top: 305px; }
  .overview--sla { top: 470px; }

  .terms { position: absolute; left: 61px; top: 577px; width: 497px; list-style: none; font-size: 15.3px; line-height: 26.2px; font-weight: 500; }
  .terms__item { position: relative; padding-left: 24px; text-align: justify; }
  .terms__tick { position: absolute; left: 0; top: 5px; width: 17px; height: 17px; }

  .after-hours {
    position: absolute; left: 61px; top: 792px; width: 411px; height: 32px;
    background: linear-gradient(90deg, var(--brand-blue), var(--brand-mid));
    color: #fff; font-weight: 700; font-size: 14.2px; line-height: 32px; padding-left: 14px;
  }

  .rates { position: absolute; left: 61px; top: 884px; width: 497px; border-collapse: separate; border-spacing: 6px 5px; margin-left: -6px; margin-top: -5px; width: 509px; }
  .rates th {
    height: 31px; background: linear-gradient(180deg, var(--brand-mid), var(--brand-blue));
    color: #fff; font-weight: 500; font-size: 15px; text-align: center;
  }
  .rates td {
    height: 31px; background: linear-gradient(180deg, var(--row-top), var(--row-bottom));
    font-size: 14px; font-weight: 500; text-align: center;
  }

  .brand { position: absolute; left: 56px; top: 1117px; display: flex; align-items: center; gap: 8px; }
  .brand__mark { width: 20px; height: 20px; background: var(--navy); }
  .brand__name { font-size: 16px; font-weight: 700; color: var(--navy); letter-spacing: 0.5px; }

  .legal { position: absolute; right: 291px; top: 1112px; font-size: 9.4px; line-height: 12px; text-align: right; font-weight: 500; }
</style>
</head>
<body>
<main class="brochure">
  <div class="brochure__photo" role="img" aria-label="Photo of a finger touching a glowing blue security padlock icon on a dark digital interface"></div>

  <h1 class="title">
    <span class="title__line--light">Block Hour</span><br>
    <span class="title__line--dark">Agreement</span>
  </h1>

  <h2 class="section-heading section-heading--overview">OVERVIEW</h2>
  <p class="overview overview--intro">Brightmoor Technologies offers the Block Time Service Agreement at a discounted hourly rate for clients who need consistent support throughout a period of time. A block time agreement lets you pre-pay for services and call upon them as needed, this allows for easy accounting and easy support. Our Block Time Service Agreement can be used for all non-project related work, please ask your Brightmoor representative for more details</p>
  <p class="overview overview--sla">Block hours are not covered under a Service Level Agreement (SLA) and are best effort, while we endeavor to always provide prompt service to our customers in some situations such as a service disruption, it may not always be possible to attend straight away.</p>

  <ul class="terms">
    <li class="terms__item"><svg class="terms__tick" viewBox="0 0 20 20"><circle cx="10" cy="10" r="8.5" fill="none" stroke="#00b2ee" stroke-width="1.8"/><path d="M5.5 10.2l3.2 3.2 7-7.5" fill="none" stroke="#00b2ee" stroke-width="2"/></svg>Block hours do not rollover</li>
    <li class="terms__item"><svg class="terms__tick" viewBox="0 0 20 20"><circle cx="10" cy="10" r="8.5" fill="none" stroke="#00b2ee" stroke-width="1.8"/><path d="M5.5 10.2l3.2 3.2 7-7.5" fill="none" stroke="#00b2ee" stroke-width="2"/></svg>There is no set usage per week.</li>
    <li class="terms__item"><svg class="terms__tick" viewBox="0 0 20 20"><circle cx="10" cy="10" r="8.5" fill="none" stroke="#00b2ee" stroke-width="1.8"/><path d="M5.5 10.2l3.2 3.2 7-7.5" fill="none" stroke="#00b2ee" stroke-width="2"/></svg>Project services cannot be used with block time.</li>
    <li class="terms__item"><svg class="terms__tick" viewBox="0 0 20 20"><circle cx="10" cy="10" r="8.5" fill="none" stroke="#00b2ee" stroke-width="1.8"/><path d="M5.5 10.2l3.2 3.2 7-7.5" fill="none" stroke="#00b2ee" stroke-width="2"/></svg>Time is billed in 0.5 hour increments with a minimum of 1 hour for onsite callouts.</li>
    <li class="terms__item"><svg class="terms__tick" viewBox="0 0 20 20"><circle cx="10" cy="10" r="8.5" fill="none" stroke="#00b2ee" stroke-width="1.8"/><path d="M5.5 10.2l3.2 3.2 7-7.5" fill="none" stroke="#00b2ee" stroke-width="2"/></svg>Hours must be used within 12 months of purchase</li>
    <li class="terms__item"><svg class="terms__tick" viewBox="0 0 20 20"><circle cx="10" cy="10" r="8.5" fill="none" stroke="#00b2ee" stroke-width="1.8"/><path d="M5.5 10.2l3.2 3.2 7-7.5" fill="none" stroke="#00b2ee" stroke-width="2"/></svg>Hours must be used during standard business hours 8:30am-5pm AWST.</li>
  </ul>

  <div class="after-hours">AFTER HOURS IS CHARGED AT DOUBLE TIME</div>

  <h2 class="section-heading section-heading--types">AGREEMENT TYPES</h2>
  <table class="rates">
    <thead>
      <tr><th>HOURS</th><th>HOURLY RATE</th><th>COST (EX GST)</th></tr>
    </thead>
    <tbody>
      <tr><td>1</td><td>$270.00</td><td>$265.00</td></tr>
      <tr><td>10</td><td>$240.00</td><td>$2,400.00</td></tr>
      <tr><td>20</td><td>$225.00</td><td>$4,500.00</td></tr>
      <tr><td>35</td><td>$220.00</td><td>$7,700.00</td></tr>
      <tr><td>50</td><td>$210.00</td><td>$10,500.00</td></tr>
    </tbody>
  </table>

  <div class="brand">
    <span class="brand__mark"></span>
    <span class="brand__name">BRIGHTMOOR</span>
  </div>

  <p class="legal">By engaging with Brightmoor in goods/services you<br>agree to our Terms and Conditions available at<br>https://www.brightmoortech.com.au/t&amp;c</p>
</main>
</body>
</html>
```